Fenwell Building Partners Stationary Revamp

We need a full set of new stationary including business cards for our Public Sector Construction company based in the South East of England. We have a new logo (attached) that we want to launch and revamp all of our company literature. We are required to send a lot of correspondence to residents etc so a consistent theme is required across everything. Also attached is our existing templates.

Target Market(s)

We work for Council and government provided housing organisations and NOT private individuals. All of our clients represent government spent money, so we need to look professional and instantly recognisable brand.

Industry/Entity Type

Business

Colors

Designer to choose colors to be used in the design.

Requirements
Must have
• New fresh designs that utilise our new logo. And the letterhead needs to be able to be rolled out onto a word template so that all staff can type straight onto it rather than us having to have it printed first.
Nice to have
• I am looking forward to seeing your best efforts as designers.

```html
<!DOCTYPE html>
<html lang="en">
<head>
<meta charset="utf-8">
<title>Fenwell Building Partners – Letterhead</title>
<link rel="stylesheet" href="https://fonts.googleapis.com/css2?family=Open+Sans:wght@400;600;700&family=Open+Sans+Condensed:wght@700&display=swap">
<style>
  :root {
    --backdrop: #d9d79a;
    --paper: #ffffff;
    --paper-edge: #f3f1d8;
    --gold: #e3ad14;
    --gold-soft: rgba(227, 173, 20, 0.08);
    --ink: #222222;
    --grey: #7a7a7a;
    --grey-bar: #8d8d8d;
    --badge: #9a9a9a;
    --badge-green: #2f8a3a;
    --badge-blue: #2a4f9c;
    --badge-red: #d3303a;
  }
  * { box-sizing: border-box; margin: 0; padding: 0; }
  html, body {
    width: 1200px; height: 784px; overflow: hidden;
    background: var(--backdrop);
    font-family: "Open Sans", Arial, sans-serif;
  }
  .stage {
    width: 1200px; height: 784px;
    display: flex; align-items: center; justify-content: center;
  }
  .letterhead {
    position: relative;
    width: 520px; height: 736px;
    background: var(--paper);
    box-shadow: 0 2px 0 var(--paper-edge), 0 4px 10px rgba(0,0,0,0.12);
    overflow: hidden;
  }
  .top-accent {
    position: absolute; top: 0; left: 300px;
    width: 70px; height: 8px; background: var(--gold);
  }
  .brand {
    position: absolute; top: 26px; right: 34px; text-align: right;
  }
  .brand-name {
    display: flex; align-items: center; justify-content: flex-end; gap: 8px;
    font-weight: 700; font-size: 17px; color: var(--ink);
  }
  .brand-dot {
    width: 12px; height: 12px; border-radius: 50%; background: var(--gold);
  }
  .brand-reg {
    margin-top: 4px; font-size: 8px; color: var(--grey); letter-spacing: 0.3px;
  }
  .contact {
    position: absolute; top: 250px; right: 34px;
    list-style: none; font-size: 8.5px; line-height: 13px; color: var(--ink);
  }
  .contact li { display: flex; align-items: center; gap: 5px; }
  .contact li::before {
    content: ""; width: 5px; height: 5px; background: var(--gold); flex: none;
  }
  .side-bar {
    position: absolute; right: 0; top: 328px;
    width: 8px; height: 60px; background: var(--grey-bar);
  }
  .watermark {
    position: absolute; top: 330px; left: 0; width: 100%;
    display: flex; align-items: center; justify-content: center; gap: 14px;
    font-weight: 700; font-size: 34px; color: var(--gold-soft);
  }
  .watermark-dot {
    width: 40px; height: 40px; border-radius: 50%; background: var(--gold-soft);
  }
  .accreditations {
    position: absolute; left: 30px; right: 30px; bottom: 56px;
    display: flex; align-items: flex-end; gap: 10px;
  }
  .cert-pair {
    display: flex; align-items: center; gap: 4px;
    border: 1px solid #c9c9c9; padding: 4px;
  }
  .cert-seal { width: 30px; height: 30px; border-radius: 50%; background: var(--badge); }
  .cert-mark { width: 24px; height: 24px; border: 1px solid var(--badge); }
  .partner-badge { width: 34px; height: 30px; }
  .partner-badge.green { background: var(--badge-green); }
  .partner-badge.blue { background: var(--badge-blue); border-radius: 50%; }
  .partner-badge.red { background: var(--badge-red); width: 44px; }
  .directors {
    position: absolute; left: 30px; bottom: 24px;
    font-family: "Open Sans Condensed", "Open Sans", sans-serif;
    font-weight: 700; font-size: 9.5px; color: var(--ink);
  }
  .directors .sep { color: var(--gold); padding: 0 3px; }
  .foot-band {
    position: absolute; left: 0; bottom: 0; width: 100%; height: 16px;
  }
</style>
</head>
<body>
<main class="stage">
  <article class="letterhead">
    <div class="top-accent"></div>

    <header class="brand">
      <div class="brand-name"><span class="brand-dot"></span>Fenwell Building Partners</div>
      <p class="brand-reg">Registration number: 09812744</p>
    </header>

    <ul class="contact">
      <li>Harlow Court, 12 Meadfield Road</li>
      <li>Ashford, Kent, TN23 4QR</li>
      <li>020 7946 0123</li>
      <li>020 7946 0188</li>
      <li>office@fenwellbp.co.uk</li>
      <li>www.fenwellbp.co.uk</li>
    </ul>
    <div class="side-bar"></div>

    <div class="watermark" aria-hidden="true">
      <span class="watermark-dot"></span>Fenwell Building Partners
    </div>

    <section class="accreditations" aria-label="Accreditations">
      <div class="cert-pair"><span class="cert-seal"></span><span class="cert-mark"></span></div>
      <div class="cert-pair"><span class="cert-seal"></span><span class="cert-mark"></span></div>
      <div class="cert-pair"><span class="cert-seal"></span><span class="cert-mark"></span></div>
      <span class="partner-badge green"></span>
      <span class="partner-badge blue"></span>
      <span class="partner-badge red"></span>
    </section>

    <p class="directors">
      Managing Director - J R Halden MIOD<span class="sep">|</span>Directors - C M Porter BSc<span class="sep">|</span>D T Marsh<span class="sep">|</span>K Ellery CMIOSH
    </p>

    <svg class="foot-band" viewBox="0 0 520 16" preserveAspectRatio="none" aria-hidden="true">
      <path d="M0 4 H330 L340 10 H520 V16 H0 Z" fill="var(--gold)"/>
    </svg>
  </article>
</main>
</body>
</html>
```